Velvet Herb Company needs a label for a new line

We need a label design for a new product that is an off shoot of Cook Tobin's Grand Zestorama Seasonings. These new spice blends will be mixed into various condiments including but not limited to ketchup, mayonnaise and butter. We really like the new Brightleaf Pecan Pouch Sack. The label has to have the 1)Cook Tobin logo on it, 2) the the name of the product which is, "Blendettes" for ketchups, Blendettes for mayonnaise and Blendettes for Sour Cream, and then underneath that,3) the flavor i.e. Honeyed Curry Sriracha etc. The labels are going to be put on bags similar to the Brightleaf Pecan Pouch Sack. We actually also like their color combinations. We are going to need to have 3 different color combos because their will be 3 different condiments to mix the product into. There will also be 2 different size black bags that the spices will go in. The 2 oz. bag is 4" W x 2 3/8" G x 6 1/2" H and the 4 oz bag is 5 1/8" W x 3 1/8" G x 8 1/8" H. So we need 3 labels that will all be the same, just the color will need to be different and name of the condiment will change.

I have attached a file with our current spice label and a picture of the Brightleaf Pecan Sack that we like.
Updates

Hi Designer, Please note in the attached file there is a small image of our product with our current logo/image of Cook Tobin. Please use this (or use image on our site http://cooktobinsgrandzestorama.example/ ) as a placeholder for the logo until we find a better/higher-res file. We may also get our printer to swap the image when we go into print production. Thanks.

Target Market(s)

Home cooks and foodies. 25 - 45 year olds

Industry/Entity Type

It Company

Font styles to use
Sans Serif

Requirements
Must have
• Cook Tobin's picture and name

```html
<!DOCTYPE html>
<html lang="en">
<head>
<meta charset="utf-8">
<title>Grand Zestorama Blendettes Label</title>
<link rel="stylesheet" href="https://fonts.googleapis.com/css2?family=Jost:wght@300;400&family=Oswald:wght@700&family=Cinzel:wght@500&display=swap">
<style>
  :root {
    --brand-red: #e3130b;
    --ink: #262626;
    --paper: #ffffff;
    --photo-dark: #1d1d1d;
  }
  * { margin: 0; padding: 0; box-sizing: border-box; }
  html, body { width: 1200px; height: 682px; overflow: hidden; background: var(--paper); }
  .label { position: relative; width: 1200px; height: 682px; background: var(--paper); }

  .brand-title { position: absolute; left: 0; top: 40px; width: 1200px; height: 110px; }
  .brand-title text { font-family: "Jost", sans-serif; font-weight: 300; fill: var(--brand-red); font-size: 116px; }

  .tagline {
    position: absolute; left: 245px; top: 154px; width: 704px;
    font-family: "Cinzel", serif; font-weight: 500; font-size: 20px;
    color: var(--brand-red); letter-spacing: 2.6px; white-space: nowrap; text-align: center;
  }
  .rule-main { position: absolute; left: 63px; top: 192px; width: 1068px; height: 7px; background: var(--ink); }

  .chef-photo {
    position: absolute; left: 63px; top: 216px; width: 369px; height: 342px;
    background: radial-gradient(ellipse at 50% 75%, #c9221a 0 22%, #e8e4df 23% 42%, var(--photo-dark) 60%);
  }
  .chef-name {
    position: absolute; left: 63px; top: 558px; width: 369px; height: 69px;
    background: var(--brand-red); color: var(--paper);
    font-family: "Jost", sans-serif; font-weight: 400; font-size: 36px; letter-spacing: 1.5px;
    display: flex; align-items: center; padding-left: 14px; gap: 10px;
  }
  .chef-name .mark { width: 24px; height: 24px; border: 2px solid var(--paper); border-radius: 50%; }

  .product-name { position: absolute; left: 456px; top: 214px; width: 676px; height: 96px; }
  .product-name text { font-family: "Oswald", sans-serif; font-weight: 700; fill: var(--ink); font-size: 110px; }
  .rule-product { position: absolute; left: 456px; top: 313px; width: 676px; height: 5px; background: var(--ink); }

  .condiment {
    position: absolute; font-family: "Jost", sans-serif; font-weight: 400; font-size: 34px;
    color: var(--ink); letter-spacing: 2.4px; white-space: nowrap; line-height: 1;
  }
  .condiment--mayo { left: 455px; top: 357px; }
  .condiment--cream { left: 557px; top: 412px; }

  .zigzag-band { position: absolute; left: 453px; top: 466px; width: 692px; height: 162px; }

  .phone {
    position: absolute; left: 800px; top: 583px;
    font-family: "Jost", sans-serif; font-weight: 400; font-size: 25px; letter-spacing: 2px; color: var(--ink);
  }
  .bags-icon { position: absolute; left: 1036px; top: 508px; width: 98px; height: 110px; }
</style>
</head>
<body>
<main class="label">
  <svg class="brand-title" viewBox="0 0 1200 110" aria-label="Grand Zestorama">
    <text x="65" y="98" textLength="1067" lengthAdjust="spacing">GRAND ZESTORAMA</text>
  </svg>
  <p class="tagline">PREMIUM SPICES FOR ALL TYPES OF COOKING</p>
  <div class="rule-main"></div>

  <div class="chef-photo" role="img" aria-label="Photo of Cook Tobin in a white chef coat, cap and red apron, smiling with open hands"></div>
  <div class="chef-name">Cook Tobin's <span class="mark"></span></div>

  <svg class="product-name" viewBox="0 0 676 96" aria-label="Blendettes">
    <text x="0" y="91" textLength="676" lengthAdjust="spacingAndGlyphs">BLENDETTES</text>
  </svg>
  <div class="rule-product"></div>

  <p class="condiment condiment--mayo">BLENDETTES FOR MAYONNAISE</p>
  <p class="condiment condiment--cream">BLENDETTES FOR SOUR CREAM</p>

  <svg class="zigzag-band" viewBox="0 0 692 162" aria-hidden="true">
    <polygon points="0,18 320,0 692,0 692,162 0,162" fill="var(--brand-red)"/>
    <polygon points="0,0 325,4 330,14 0,8" fill="var(--ink)"/>
    <polygon points="330,14 300,14 0,128 0,150 70,140 692,10 692,0 560,6" fill="var(--ink)"/>
    <polygon points="0,128 300,14 330,14 20,132" fill="var(--paper)"/>
    <polygon points="0,150 70,140 692,10 692,18 100,150 0,162" fill="var(--paper)"/>
  </svg>

  <p class="phone">(555) 014-3927</p>
  <svg class="bags-icon" viewBox="0 0 98 110" aria-hidden="true">
    <g fill="none" stroke="var(--paper)" stroke-width="4">
      <path d="M50 24 v-8 a10 10 0 0 1 20 0 v8"/>
      <path d="M14 38 v-8 a9 9 0 0 1 18 0 v8"/>
    </g>
    <polygon points="42,24 96,24 90,104 48,104" fill="var(--paper)"/>
    <polygon points="2,38 44,38 46,108 6,108" fill="var(--paper)" stroke="var(--brand-red)" stroke-width="2"/>
  </svg>
</main>
</body>
</html>
```